Complete Stationary Package for Sea Harvest Trading Company
Silver Lantern Sea Harvest 銀燈海珍
Complete Stationary Package for Sea Harvest Trading Company - Food
Creative Brief
Simple
Malcolm Whitby 马尔
Director of Sales and Distribution
Silver Lantern Sea Harvest, Level 11, KL Plaza 5, Jalan Kenari Raya, Bangsar, 59100 Kuala Lumpur, Malaysia
mwhitby@slseaharvest-example.com
www.slseaharvest-example.com
We need a full stationary package design - business cards, letterhead, envelopes, folders, invoice, email signature and any other standard stationary items you may decide to include in your concepts. I need the text below written in smaller print somewhere on the card either on the front or the back " Silver Lantern Sea Harvest is a registered trademark of Corvale Holdings Sdn Bhd 8827165K". I like the same cream colour that is used in the packaging that I have uploaded. I do not want the card to have a white background colour. I would like red and/or gold to feature also.
I would like a suitable design for the back of the card with the company name and logo.

```html
<!DOCTYPE html>
<html lang="en">
<head>
<meta charset="UTF-8">
<title>Silver Lantern Sea Harvest — Business Card</title>
<link rel="stylesheet" href="https://fonts.googleapis.com/css2?family=Raleway:wght@400;500;600&family=Noto+Sans+TC:wght@500&display=swap">
<style>
  :root {
    --backdrop: #6f6a62;
    --card-red: #c8141c;
    --card-red-deep: #a80e15;
    --cream: #f1e9d8;
    --gold: #b8893a;
    --gold-light: #e0c58a;
    --ink-red: #c8141c;
    --ink-grey: #7d7468;
    --on-red: #f6e6c8;
  }
  * { box-sizing: border-box; margin: 0; padding: 0; }
  html, body {
    width: 1200px; height: 904px; overflow: hidden;
    background: var(--backdrop);
    font-family: "Raleway", "Noto Sans TC", sans-serif;
  }
  .stage {
    width: 1200px; height: 904px;
    display: flex; align-items: center; justify-content: center; gap: 80px;
  }
  .card {
    width: 400px; height: 680px;
    border-radius: 4px;
    box-shadow: 0 18px 40px rgba(0,0,0,.35);
    position: relative;
  }

  /* back of card */
  .card-back {
    background: linear-gradient(160deg, var(--card-red) 0%, var(--card-red-deep) 100%);
    display: flex; flex-direction: column; align-items: center; justify-content: center;
    color: var(--on-red);
  }
  .brand-mark {
    width: 150px; height: 150px; border-radius: 50%;
    background: var(--on-red);
    margin-bottom: 28px;
  }
  .brand-name {
    font-weight: 500; text-align: center; letter-spacing: .18em;
    text-transform: uppercase; font-size: 15px; line-height: 1.7;
  }
  .brand-name .brand-cn { display: block; font-size: 34px; letter-spacing: .25em; margin-bottom: 6px; }
  .trademark {
    position: absolute; bottom: 40px; left: 0; right: 0;
    text-align: center; font-size: 10.5px; letter-spacing: .04em; line-height: 1.6;
    padding: 0 40px; color: var(--on-red);
  }

  /* front of card */
  .card-front {
    background: var(--cream);
    padding: 56px 44px;
    display: flex; flex-direction: column;
  }
  .front-brand {
    display: flex; align-items: center; gap: 18px; margin-bottom: 70px;
    color: var(--gold);
  }
  .front-brand .brand-mark {
    width: 92px; height: 92px; margin: 0;
    background: var(--gold);
  }
  .front-brand .brand-name { text-align: left; font-size: 11px; letter-spacing: .14em; }
  .front-brand .brand-name .brand-cn { font-size: 26px; letter-spacing: .2em; margin-bottom: 4px; }

  .person-name { color: var(--ink-red); font-size: 24px; font-weight: 600; letter-spacing: .02em; }
  .person-name .cn { font-size: 18px; font-weight: 500; margin-left: 6px; }
  .person-title { color: var(--gold); font-size: 13px; font-weight: 500; margin-top: 6px; letter-spacing: .03em; }

  .address {
    font-style: normal; margin-top: 40px;
    color: var(--ink-grey); font-size: 13px; line-height: 1.75;
  }
  .contact { list-style: none; margin-top: 28px; color: var(--ink-grey); font-size: 13px; line-height: 2; }
  .contact li { display: flex; align-items: center; gap: 10px; }
  .contact .label { color: var(--gold); font-weight: 600; width: 14px; }
</style>
</head>
<body>
<main class="stage">

  <section class="card card-back" aria-label="Card back">
    <div class="brand-mark" aria-hidden="true"></div>
    <p class="brand-name"><span class="brand-cn">銀燈海珍</span>Silver Lantern Sea Harvest</p>
    <p class="trademark">Silver Lantern Sea Harvest is a registered trademark of Corvale Holdings Sdn Bhd 8827165K</p>
  </section>

  <section class="card card-front" aria-label="Card front">
    <div class="front-brand">
      <div class="brand-mark" aria-hidden="true"></div>
      <p class="brand-name"><span class="brand-cn">銀燈海珍</span>Silver Lantern<br>Sea Harvest</p>
    </div>

    <h1 class="person-name">Malcolm Whitby <span class="cn">马尔</span></h1>
    <p class="person-title">Director of Sales and Distribution</p>

    <address class="address">
      Silver Lantern Sea Harvest<br>
      Level 11, KL Plaza 5,<br>
      Jalan Kenari Raya, Bangsar,<br>
      59100 Kuala Lumpur,<br>
      Malaysia
    </address>

    <ul class="contact">
      <li><span class="label">T</span>+60 3-2274 5510</li>
      <li><span class="label">M</span>+60 12-408 3362</li>
      <li><span class="label">E</span>mwhitby@slseaharvest-example.com</li>
      <li><span class="label">W</span>www.slseaharvest-example.com</li>
    </ul>
  </section>

</main>
</body>
</html>
```